Magician | Speaker looks for an innovative business card design

I'm a magician and public speaker offering artistic and modern magical experiences.
I'm based in Brussels (Belgium.) I love magic performed up-close, creating a space of intimacy, even when I'm on stage.
The final design should communicate professionalism, elegance, artistry, and a friendly kind personality

I would like to see designs based either on my photos and/or the way I sign my name Theo Varn (see attached files for more info.)
Additional photos and more info about what I offer can be seen at www.theo-varn.net

My current business card design is also attached. I like the fact that the reverse of my current design includes quotes from master magicians about magic, changing the way my participants see the art of magic.

Note: I would like a double-sided card design. However, I need white space on the reverse to be able to write things on for my performances.

Details to include on the card:
Artist name: Theo Varn
Offer: magician + (public) speaker or magic + (public) speaking (the + sign can be replaced by another character, like a bullet or a pipe)
Phone: +32 471 236 519
Email: book@theo-varn.net
(optional) Website: www.theo-varn.net or theo-varn.net

Target Market(s)

Corporate, organisations, companies as well as individuals

Industry/Entity Type

Artists

Colors

Designer to choose colors to be used in the design.

Requirements
Nice to have
• A side with a mirror could be nice

```html
<!DOCTYPE html>
<html lang="en">
<head>
<meta charset="utf-8">
<title>Theo Varn – Business Card</title>
<link rel="stylesheet" href="https://fonts.googleapis.com/css2?family=Cinzel:wght@500;700&family=Montserrat:wght@400;600&display=swap">
<style>
  :root{
    --bg:#e9e6e1;
    --front-ink:#241f1b;
    --front-deep:#17130f;
    --gold:#d8c9a6;
    --cream:#f1ede4;
    --paper:#efece5;
    --ink:#1c1a18;
    --red:#c8342d;
    --line:#8d8578;
  }
  *{margin:0;padding:0;box-sizing:border-box}
  html,body{width:1200px;height:960px;overflow:hidden;background:var(--bg)}
  .canvas{position:relative;width:1200px;height:960px}
  .card{position:absolute;top:160px;width:380px;height:640px;border-radius:14px;overflow:hidden;box-shadow:0 10px 30px rgba(0,0,0,.18)}

  /* front */
  .card--front{left:170px;background:radial-gradient(ellipse at 50% 45%,#3a322b 0%,var(--front-ink) 55%,var(--front-deep) 100%)}
  .front__frame{position:absolute;inset:16px;border:1.5px solid rgba(216,201,166,.55);border-radius:12px}
  .front__pattern{position:absolute;left:50%;top:50%;width:300px;height:520px;transform:translate(-50%,-50%);
    background:radial-gradient(circle at 50% 50%,rgba(216,201,166,.16) 0%,rgba(216,201,166,.05) 45%,transparent 70%)}
  .front__title{position:absolute;left:0;right:0;text-align:center;font-family:"Cinzel",serif;font-weight:700;color:var(--gold);letter-spacing:.14em}
  .front__title--top{top:132px;font-size:30px}
  .front__name{position:absolute;left:0;right:0;top:292px;text-align:center;font-family:"Cinzel",serif;font-weight:700;font-size:48px;color:var(--cream);letter-spacing:.04em}
  .front__sub{position:absolute;left:0;right:0;top:476px;text-align:center;font-family:"Cinzel",serif;font-weight:500;font-size:22px;color:var(--red);letter-spacing:.14em}
  .front__title--bottom{top:506px;font-size:32px;letter-spacing:.2em}

  /* back */
  .card--back{left:650px;background:var(--paper)}
  .back__index{position:absolute;font-family:"Cinzel",serif;font-weight:700;font-size:26px;color:var(--red);text-align:center;width:28px;line-height:1}
  .back__index svg{display:block;margin:4px auto 0}
  .back__index--top{left:20px;top:22px}
  .back__index--bottom{right:20px;bottom:22px;transform:rotate(180deg)}
  .back__spade{position:absolute;left:50%;top:40px;transform:translateX(-50%)}
  .back__name{position:absolute;left:0;right:0;top:138px;text-align:center;font-family:"Cinzel",serif;font-weight:700;font-size:38px;color:var(--cream)}
  .back__band{position:absolute;left:50%;transform:translateX(-50%);background:var(--ink);color:var(--cream);font-family:"Montserrat",sans-serif;font-weight:600;letter-spacing:.08em;text-align:center;padding:4px 0}
  .back__band--one{top:252px;width:200px;font-size:18px}
  .back__amp{position:absolute;left:0;right:0;top:281px;text-align:center;font-family:"Cinzel",serif;font-size:18px;color:var(--red)}
  .back__band--two{top:304px;width:280px;font-size:18px}
  .back__label{position:absolute;left:50%;transform:translateX(-50%);width:240px;display:flex;align-items:center;gap:8px;font-family:"Montserrat",sans-serif;font-size:15px;color:var(--ink);letter-spacing:.06em}
  .back__label::before,.back__label::after{content:"";flex:1;height:1px;background:var(--ink)}
  .back__label--phone{top:358px}
  .back__label--mail{top:420px}
  .back__value{position:absolute;left:0;right:0;text-align:center;font-family:"Montserrat",sans-serif;font-weight:600;color:var(--ink)}
  .back__value--phone{top:376px;font-size:24px}
  .back__value--mail{top:438px;font-size:22px}
  .back__flourish{position:absolute;left:50%;top:480px;width:120px;height:22px;transform:translateX(-50%);background:linear-gradient(90deg,transparent,rgba(28,26,24,.55),transparent);border-radius:11px}
  .back__web{position:absolute;left:26px;bottom:20px;transform-origin:left bottom;transform:rotate(-90deg) translateY(100%);font-family:"Montserrat",sans-serif;font-size:13px;color:var(--ink);white-space:nowrap}
</style>
</head>
<body>
<main class="canvas">
  <section class="card card--front">
    <div class="front__pattern" role="img" aria-label="Faint geometric circle and star line pattern"></div>
    <div class="front__frame"></div>
    <p class="front__title front__title--top">MAGICIAN</p>
    <p class="front__name">Theo Varn</p>
    <p class="front__sub">PUBLIC</p>
    <p class="front__title front__title--bottom">SPEAKER</p>
  </section>

  <section class="card card--back">
    <div class="back__index back__index--top">A
      <svg width="18" height="20" viewBox="0 0 18 20"><path d="M9 0C6 5 0 8 0 12.5 0 15 2 16.5 4 16.5c1.6 0 2.8-.8 3.6-1.8L6.5 20h5l-1.1-5.3c.8 1 2 1.8 3.6 1.8 2 0 4-1.5 4-4C18 8 12 5 9 0Z" fill="#1c1a18"/></svg>
    </div>
    <svg class="back__spade" width="240" height="240" viewBox="0 0 240 240" role="img" aria-label="Large spade filled with a fine line pattern">
      <path d="M120 0C90 50 8 88 8 142c0 32 24 52 54 52 22 0 38-10 48-24l-14 70h48l-14-70c10 14 26 24 48 24 30 0 54-20 54-52C232 88 150 50 120 0Z" fill="#2a2622"/>
    </svg>
    <p class="back__name">Theo Varn</p>
    <p class="back__band back__band--one">MAGICIAN</p>
    <p class="back__amp">&amp;</p>
    <p class="back__band back__band--two">PUBLIC SPEAKER</p>
    <p class="back__label back__label--phone">PHONE</p>
    <p class="back__value back__value--phone">+32 471 236 519</p>
    <p class="back__label back__label--mail">E-MAIL</p>
    <p class="back__value back__value--mail">book@theo-varn.net</p>
    <div class="back__flourish" role="img" aria-label="Small ornamental flourish"></div>
    <p class="back__web">www.theo-varn.net</p>
    <div class="back__index back__index--bottom">A
      <svg width="18" height="20" viewBox="0 0 18 20"><path d="M9 0C6 5 0 8 0 12.5 0 15 2 16.5 4 16.5c1.6 0 2.8-.8 3.6-1.8L6.5 20h5l-1.1-5.3c.8 1 2 1.8 3.6 1.8 2 0 4-1.5 4-4C18 8 12 5 9 0Z" fill="#1c1a18"/></svg>
    </div>
  </section>
</main>
</body>
</html>
```